Hair & Skin Product Line

I need someone to design clear product labels that can go on pink bottles. I'm looking for someone who can add graphics such as avocado and honey to the label as these are ingredients in our products. The colors we want incorporated are gold, blue, white and purple. I will upload information about our company identity and information on one label. Whoever we choose, we will use them to create 11 more labels.

Target Market(s)

Woman 25-50, Natural, straight or curly hair.

Industry/Entity Type

Beauty

```html
<!DOCTYPE html>
<html lang="en">
<head>
<meta charset="utf-8">
<title>Moisture Repair Shampoo Label</title>
<link href="https://fonts.googleapis.com/css2?family=Montserrat:wght@700&family=Raleway:wght@500&family=Marcellus&family=Oswald:wght@500&display=swap" rel="stylesheet">
<style>
  :root {
    --bg-left: #fb8cff;
    --bg-right: #ffe2ff;
    --label-white: #ffffff;
    --label-cream: #faf0a2;
    --label-gold: #f1d462;
    --leaf-dark: #1b6b21;
    --leaf-light: #7cc25a;
    --band-deep: #2b8429;
    --band-glow: #b6e98a;
    --art-tone: #9fd476;
    --gold-foil: #e3b63c;
  }
  html, body {
    margin: 0;
    padding: 0;
    width: 1200px;
    height: 953px;
    overflow: hidden;
  }
  body {
    background: linear-gradient(90deg, var(--bg-left), var(--bg-right));
  }
  .label-art {
    display: block;
    width: 1200px;
    height: 953px;
  }
  .brand-arc {
    font-family: "Montserrat", sans-serif;
    font-weight: 700;
    font-size: 22px;
    letter-spacing: 3px;
    fill: var(--leaf-dark);
  }
  .product-line {
    font-family: "Raleway", sans-serif;
    font-weight: 500;
    font-size: 19px;
    letter-spacing: 2px;
    fill: var(--leaf-dark);
  }
  .product-type {
    font-family: "Marcellus", serif;
    font-size: 56px;
    fill: url(#goldFoilText);
  }
  .infusion {
    font-family: "Oswald", sans-serif;
    font-weight: 500;
    font-size: 20px;
    fill: var(--leaf-dark);
  }
  .benefit {
    font-family: "Raleway", sans-serif;
    font-weight: 500;
    font-size: 14px;
    fill: var(--leaf-dark);
  }
  .volume {
    font-family: "Oswald", sans-serif;
    font-weight: 500;
    font-size: 12px;
    fill: var(--leaf-dark);
  }
  .star-dark { fill: var(--leaf-dark); }
  .star-light { fill: var(--leaf-light); }
  .dot { fill: var(--leaf-dark); }
</style>
</head>
<body>
<svg class="label-art" viewBox="0 0 1200 953" xmlns="http://www.w3.org/2000/svg">
  <defs>
    <linearGradient id="creamFill" x1="0" y1="0" x2="0" y2="1">
      <stop offset="0" stop-color="var(--label-gold)"/>
      <stop offset="0.2" stop-color="var(--label-cream)"/>
      <stop offset="0.8" stop-color="var(--label-cream)"/>
      <stop offset="1" stop-color="var(--label-gold)"/>
    </linearGradient>
    <radialGradient id="bandFill" cx="0.5" cy="0.62" r="0.65">
      <stop offset="0" stop-color="var(--band-glow)"/>
      <stop offset="1" stop-color="var(--band-deep)"/>
    </radialGradient>
    <linearGradient id="goldFoilText" x1="0" y1="0" x2="1" y2="0">
      <stop offset="0" stop-color="#f3d36a"/>
      <stop offset="0.5" stop-color="var(--gold-foil)"/>
      <stop offset="1" stop-color="#d7922e"/>
    </linearGradient>
    <linearGradient id="goldFoilRule" gradientUnits="userSpaceOnUse" x1="409" y1="0" x2="795" y2="0">
      <stop offset="0" stop-color="#f3d36a"/>
      <stop offset="0.5" stop-color="var(--gold-foil)"/>
      <stop offset="1" stop-color="#d7922e"/>
    </linearGradient>
    <filter id="labelShadow" x="-10%" y="-10%" width="120%" height="120%">
      <feDropShadow dx="4" dy="8" stdDeviation="10" flood-color="#a04aa8" flood-opacity="0.45"/>
    </filter>
    <clipPath id="innerClip">
      <rect x="350" y="66" width="500" height="821" rx="250"/>
    </clipPath>
    <path id="brandCurve" d="M 441 319 A 159 159 0 0 1 759 319"/>
    <polygon id="star" points="0,-9 2.6,-2.8 8.6,-2.8 3.8,1.1 5.5,7.3 0,3.6 -5.5,7.3 -3.8,1.1 -8.6,-2.8 -2.6,-2.8"/>
  </defs>

  <!-- label body -->
  <rect x="318" y="36" width="564" height="881" rx="282" fill="var(--label-white)" filter="url(#labelShadow)"/>
  <rect x="334" y="52" width="532" height="849" rx="266" fill="url(#creamFill)"/>

  <!-- green band -->
  <rect x="350" y="285" width="500" height="384" fill="url(#bandFill)" clip-path="url(#innerClip)"/>
  <line x1="350" y1="285" x2="850" y2="285" stroke="var(--leaf-dark)" stroke-width="2"/>
  <line x1="350" y1="669" x2="850" y2="669" stroke="var(--leaf-dark)" stroke-width="2"/>
  <rect x="350" y="66" width="500" height="821" rx="250" fill="none" stroke="var(--leaf-dark)" stroke-width="2.5"/>

  <!-- top stars -->
  <use href="#star" class="star-light" x="537" y="126"/>
  <use href="#star" class="star-light" x="567" y="109"/>
  <use href="#star" class="star-light" x="602" y="103"/>
  <use href="#star" class="star-dark" x="636" y="109"/>
  <use href="#star" class="star-dark" x="666" y="126"/>

  <!-- brand -->
  <text class="brand-arc" text-anchor="middle">
    <textPath href="#brandCurve" startOffset="50%">GROVE &amp; NECTAR</textPath>
  </text>
  <g class="dots-top">
    <circle class="dot" cx="572" cy="199" r="3.2"/>
    <circle class="dot" cx="587" cy="199" r="3.2"/>
    <circle class="dot" cx="602" cy="199" r="3.2"/>
    <circle class="dot" cx="617" cy="199" r="3.2"/>
    <circle class="dot" cx="632" cy="199" r="3.2"/>
  </g>

  <!-- product line -->
  <line x1="449" y1="242" x2="498" y2="242" stroke="var(--leaf-dark)" stroke-width="2"/>
  <text class="product-line" x="601" y="249" text-anchor="middle">MOISTURE REPAIR</text>
  <line x1="704" y1="242" x2="753" y2="242" stroke="var(--leaf-dark)" stroke-width="2"/>

  <!-- product type -->
  <line x1="409" y1="309" x2="795" y2="309" stroke="url(#goldFoilRule)" stroke-width="2"/>
  <text class="product-type" x="600" y="359" text-anchor="middle">SHAMPOO</text>
  <line x1="409" y1="368" x2="795" y2="368" stroke="url(#goldFoilRule)" stroke-width="2"/>

  <!-- ingredient artwork area -->
  <rect x="423" y="405" width="358" height="218" rx="16" fill="var(--art-tone)" opacity="0.55"
        role="img" aria-label="Ingredient artwork: honeycomb, halved avocado, cucumber slice and mint leaves"/>

  <!-- infusion pill -->
  <rect x="476" y="651" width="275" height="34" rx="17" fill="var(--label-cream)" stroke="var(--leaf-dark)" stroke-width="2"/>
  <text class="infusion" x="613" y="676" text-anchor="middle">INFUSED W/BIOTIN + ROSEMARY</text>

  <g class="dots-bottom">
    <circle class="dot" cx="572" cy="716" r="3.2"/>
    <circle class="dot" cx="587" cy="716" r="3.2"/>
    <circle class="dot" cx="602" cy="716" r="3.2"/>
    <circle class="dot" cx="617" cy="716" r="3.2"/>
    <circle class="dot" cx="632" cy="716" r="3.2"/>
  </g>

  <!-- benefit copy -->
  <text class="benefit" x="602" y="755" text-anchor="middle">GENTLY CLEANSES AND HYDRATES FOR RETENTION,</text>
  <text class="benefit" x="602" y="776" text-anchor="middle">MOISTURE AND SOFTNESS</text>

  <!-- volume -->
  <text class="volume" x="602" y="816" text-anchor="middle">300 ML /10 FL OZ</text>

  <!-- bottom stars -->
  <use href="#star" class="star-dark" x="537" y="822"/>
  <use href="#star" class="star-dark" x="567" y="840"/>
  <use href="#star" class="star-light" x="602" y="846"/>
  <use href="#star" class="star-light" x="636" y="840"/>
  <use href="#star" class="star-light" x="666" y="822"/>
</svg>
</body>
</html>
```